Service business needs Business Card Design

Looking to create a new business card design that is both professional and unique the can highlight the many services we offer throughout the seasons. Our tagline is "The Cobalt Advantage"
Licensed & Insured: HC731462 has to be small and on the back side of the card.
On the Front:
FirstName LastName
Title
We offer the following services:
Deck Repair and Maintenance
Deck Cleaning and Staining/Painting
Power Washing/House Washing
Landscape Lighting Installation
Christmas Lighting Installation

```html
<!DOCTYPE html>
<html lang="en">
<head>
<meta charset="utf-8">
<title>Harbor Ridge Services – Business Card</title>
<link rel="stylesheet" href="https://fonts.googleapis.com/css2?family=Arimo:wght@400;700&family=Michroma&display=swap">
<style>
  :root {
    --page-bg: #2a2a2a;
    --card-bg: #0b0b0c;
    --blue-deep: #1f6fc0;
    --blue-bright: #37a8e6;
    --text-white: #f2f4f6;
    --divider: #555a60;
  }
  * { box-sizing: border-box; margin: 0; padding: 0; }
  html, body { width: 1200px; height: 900px; overflow: hidden; }
  body {
    background: var(--page-bg);
    font-family: "Arimo", Arial, sans-serif;
    display: flex;
    align-items: center;
    justify-content: center;
    gap: 40px;
  }
  .card {
    width: 540px;
    height: 309px;
    background: var(--card-bg);
    position: relative;
    box-shadow: 0 10px 30px rgba(0,0,0,.5);
  }

  /* Back side */
  .card-back .brand {
    position: absolute;
    left: 34px; top: 108px;
    width: 220px;
    display: flex; align-items: center; gap: 10px;
  }
  .brand-dot {
    width: 16px; height: 16px; border-radius: 50%;
    background: var(--blue-deep); flex: none;
  }
  .brand-name {
    font-weight: 700; font-size: 24px; line-height: 1.1;
    color: var(--blue-deep); letter-spacing: .5px;
  }
  .card-back .divider {
    position: absolute; left: 262px; top: 58px;
    width: 1px; height: 150px; background: var(--divider);
  }
  .contact {
    position: absolute; left: 286px; top: 62px;
    color: var(--text-white);
  }
  .person-name {
    font-weight: 700; font-size: 17px; color: var(--blue-deep);
    letter-spacing: .5px; text-transform: uppercase;
  }
  .person-title { font-size: 14px; margin-bottom: 14px; }
  .contact-line {
    display: flex; align-items: center; gap: 8px;
    font-size: 14px; line-height: 20px;
  }
  .contact-line svg { width: 13px; height: 13px; flex: none; }
  .accent { color: var(--blue-deep); }
  .license { margin-top: 16px; font-size: 14px; }
  .license .accent { color: var(--blue-bright); }
  .tagline {
    position: absolute; left: 0; right: 0; bottom: 36px;
    text-align: center;
    font-family: "Michroma", Arial, sans-serif;
    font-size: 15px; color: var(--blue-bright);
    text-transform: uppercase; letter-spacing: 1px;
  }

  /* Front side */
  .card-front {
    display: flex; flex-direction: column; align-items: center;
    padding-top: 66px; text-align: center;
  }
  .card-front .brand { display: flex; align-items: center; gap: 10px; margin-bottom: 26px; }
  .card-front .brand-name { font-size: 28px; }
  .services-heading {
    font-size: 14px; color: var(--blue-bright);
    text-transform: uppercase; margin-bottom: 6px;
  }
  .services { list-style: none; font-size: 13.5px; line-height: 19px; color: var(--text-white); }
  .sep { color: var(--blue-bright); padding: 0 3px; }
</style>
</head>
<body>
  <section class="card card-back">
    <div class="brand">
      <span class="brand-dot"></span>
      <span class="brand-name">Harbor Ridge Services</span>
    </div>
    <div class="divider"></div>
    <div class="contact">
      <p class="person-name">Marcus Ellery</p>
      <p class="person-title">Managing Director</p>
      <p class="contact-line">
        <svg viewBox="0 0 16 16" fill="none" stroke="#37a8e6" stroke-width="1.6"><path d="M3 2l3 1 1 3-2 1a8 8 0 0 0 4 4l1-2 3 1 1 3-2 1C7 14 2 9 2 4z"/></svg>
        044-987 654 321
      </p>
      <p class="contact-line">
        <svg viewBox="0 0 16 16" fill="none" stroke="#37a8e6" stroke-width="1.6"><rect x="1.5" y="3.5" width="13" height="9"/><path d="M1.5 3.5l6.5 5 6.5-5"/></svg>
        hello@ridgemail.com
      </p>
      <p class="contact-line">
        <svg viewBox="0 0 16 16" fill="none" stroke="#37a8e6" stroke-width="1.4"><circle cx="8" cy="8" r="6.5"/><ellipse cx="8" cy="8" rx="3" ry="6.5"/><path d="M1.5 8h13M2.5 4.7h11M2.5 11.3h11"/></svg>
        <span>www.<span class="accent">harborridgepro</span>.com</span>
      </p>
      <p class="license"><span class="accent">Licensed &amp; Insured</span>: HC731462</p>
    </div>
    <p class="tagline">The Cobalt Advantage</p>
  </section>

  <section class="card card-front">
    <div class="brand">
      <span class="brand-dot"></span>
      <span class="brand-name">Harbor Ridge Services</span>
    </div>
    <p class="services-heading">We offer the following services</p>
    <ul class="services">
      <li>Deck Repair and Maintenance <span class="sep">|</span> Deck Cleaning and Staining/Painting</li>
      <li>Power Washing/House Washing <span class="sep">|</span> Landscape Lighting Installation</li>
      <li>Christmas Lighting Installation</li>
    </ul>
  </section>
</body>
</html>
```